Display Layouts per segment use-cases

21.5in portrait (9:16) x 2
Office towers
Hotels
Shopping Malls

Target Market(s)

Office towers / Hotels / Shopping Malls

```html
<!DOCTYPE html>
<html lang="en">
<head>
<meta charset="utf-8">
<title>Display Layouts per Segment</title>
<link href="https://fonts.googleapis.com/css2?family=Montserrat:wght@300;400;500;600;800&display=swap" rel="stylesheet">
<style>
  :root {
    --bg: #2f1212;
    --title: #f4ecea;
    --white: #ffffff;
    --office-band: #3b8fd8;
    --office-band-light: #5eaef0;
    --office-strip: #4fc6cf;
    --office-accent: #26b3b6;
    --office-accent-dark: #1f8e95;
    --hotel-band: #8a6a55;
    --hotel-band-light: #c9ad93;
    --hotel-accent: #dc5e13;
    --hotel-accent-dark: #b8480b;
    --mall-band: #17904f;
    --mall-band-light: #3fb06f;
    --mall-accent: #13a04d;
    --mall-accent-dark: #0b7d3a;
  }
  * { box-sizing: border-box; margin: 0; padding: 0; }
  html, body { width: 1200px; height: 673px; overflow: hidden; background: var(--bg); }
  .canvas { position: relative; width: 1200px; height: 673px; background: var(--bg); font-family: "Montserrat", sans-serif; }

  .segment-title {
    position: absolute; top: 80px; width: 300px; text-align: center;
    color: var(--title); font-weight: 400; font-size: 20px; letter-spacing: 1px;
    font-variant: small-caps;
  }

  .display { position: absolute; top: 127px; width: 268px; height: 476px; overflow: hidden; }
  .display--office { left: 107px; }
  .display--hotel { left: 464px; }
  .display--mall { left: 826px; }

  .photo { position: absolute; top: 0; height: 100%; }
  .info-band { position: absolute; top: 0; height: 100%; }
  .strip { position: absolute; top: 0; height: 100%; }

  .display--office .info-band { left: 0; width: 97px; background: linear-gradient(180deg, var(--office-band) 0%, var(--office-band-light) 45%, var(--office-band) 100%); }
  .display--office .strip { left: 97px; width: 14px; background: var(--office-strip); opacity: .85; }
  .display--office .photo { left: 111px; width: 157px; background: linear-gradient(180deg, #1e9be0 0%, #7fbfe0 25%, #3d6f92 55%, #6d7f86 80%, #c9c1b6 100%); }

  .display--hotel .photo { left: 0; width: 154px; background: linear-gradient(90deg, #7a2f12 0%, #c6713a 35%, #e7b98c 55%, #b0622e 80%, #8a4a2a 100%); }
  .display--hotel .strip { left: 154px; width: 12px; background: linear-gradient(90deg, #a87452, #7a5640); }
  .display--hotel .info-band { left: 166px; width: 102px; background: linear-gradient(90deg, var(--hotel-band) 0%, var(--hotel-band-light) 100%); }

  .display--mall .photo { left: 0; width: 154px; background: linear-gradient(180deg, #dff2ea 0%, #b7e0cf 35%, #8fc7ad 60%, #c08a5e 85%, #9a6b4c 100%); }
  .display--mall .strip { left: 154px; width: 13px; background: var(--mall-band-light); opacity: .8; }
  .display--mall .info-band { left: 167px; width: 101px; background: linear-gradient(180deg, var(--mall-band) 0%, var(--mall-band-light) 100%); }

  .brand { position: absolute; top: 28px; font-weight: 800; font-size: 21px; line-height: 1; color: var(--white); letter-spacing: -0.3px; white-space: nowrap; }
  .weather-icon { position: absolute; top: 126px; width: 62px; height: 52px; }
  .temp { position: absolute; top: 180px; color: var(--white); font-weight: 500; font-size: 36px; line-height: 1; letter-spacing: -1px; white-space: nowrap; }
  .temp .unit { font-size: 22px; }
  .temp .deg { font-size: 22px; vertical-align: 12px; }
  .clock { position: absolute; top: 252px; color: var(--white); font-weight: 500; font-size: 23px; line-height: 1.1; letter-spacing: -0.5px; white-space: nowrap; }
  .clock .meridiem { font-size: 10px; font-weight: 400; vertical-align: 10px; margin-left: 1px; }
  .display--office .clock { border-bottom: 1px solid rgba(255,255,255,.8); padding-bottom: 1px; }
  .weekday { position: absolute; top: 281px; color: var(--white); font-weight: 300; font-size: 9px; white-space: nowrap; }
  .date { position: absolute; top: 292px; color: var(--white); font-weight: 600; font-size: 13px; white-space: nowrap; }

  .display--office .brand { left: 7px; }
  .display--office .weather-icon,
  .display--office .temp,
  .display--office .clock,
  .display--office .weekday,
  .display--office .date { left: 10px; }
  .display--hotel .brand { left: 172px; }
  .display--hotel .weather-icon,
  .display--hotel .temp,
  .display--hotel .clock,
  .display--hotel .weekday,
  .display--hotel .date { left: 180px; }
  .display--mall .brand { left: 173px; }
  .display--mall .weather-icon,
  .display--mall .temp,
  .display--mall .clock,
  .display--mall .weekday,
  .display--mall .date { left: 180px; }

  .wayfinder { position: absolute; top: 346px; width: 124px; height: 124px; }
  .display--office .wayfinder { left: 117px; }
  .display--hotel .wayfinder, .display--mall .wayfinder { left: 13px; }
  .wayfinder text { font-family: "Montserrat", sans-serif; font-weight: 600; font-size: 40px; }
</style>
</head>
<body>
<main class="canvas">

  <h2 class="segment-title" style="left:90px">Office towers</h2>
  <h2 class="segment-title" style="left:447px">Hotels</h2>
  <h2 class="segment-title" style="left:810px">Shopping Malls</h2>

  <section class="display display--office">
    <div class="photo" role="img" aria-label="Glass office tower with palm trees under a blue sky"></div>
    <div class="info-band"></div>
    <div class="strip"></div>
    <div class="brand">VELORA</div>
    <svg class="weather-icon" viewBox="0 0 62 52" aria-label="Partly cloudy">
      <g stroke="#fff" stroke-width="2" stroke-linecap="round">
        <line x1="18" y1="2" x2="18" y2="7"/><line x1="7" y1="7" x2="10" y2="10"/>
        <line x1="29" y1="7" x2="26" y2="10"/><line x1="2" y1="18" x2="6" y2="18"/>
        <line x1="7" y1="29" x2="10" y2="26"/>
      </g>
      <circle cx="18" cy="18" r="8" fill="#fff"/>
      <path d="M14 48 a9 9 0 0 1 2 -17 a13 13 0 0 1 25 -4 a10 10 0 0 1 17 8 a7 7 0 0 1 -2 13 z" fill="#fff" stroke="var(--office-band)" stroke-width="1.5"/>
    </svg>
    <div class="temp">26<span class="deg">°</span><span class="unit">C</span></div>
    <div class="clock">07:15<span class="meridiem">PM</span></div>
    <div class="weekday">MONDAY</div>
    <div class="date">15 AUGUST</div>
    <svg class="wayfinder" viewBox="0 0 124 124" aria-label="Floor 5 up">
      <circle cx="60" cy="64" r="60" fill="var(--office-accent)"/>
      <circle cx="64" cy="60" r="56" fill="#fff"/>
      <polygon points="62,10 30,72 62,60" fill="var(--office-accent)"/>
      <polygon points="62,10 94,72 62,60" fill="var(--office-accent-dark)"/>
      <text x="62" y="110" text-anchor="middle" fill="var(--office-accent)">5</text>
    </svg>
  </section>

  <section class="display display--hotel">
    <div class="photo" role="img" aria-label="Warm-lit hotel corridor with wooden doors and tiled floor"></div>
    <div class="strip"></div>
    <div class="info-band"></div>
    <div class="brand">VELORA</div>
    <svg class="weather-icon" viewBox="0 0 62 52" aria-label="Partly cloudy">
      <g stroke="#fff" stroke-width="2" stroke-linecap="round">
        <line x1="18" y1="2" x2="18" y2="7"/><line x1="7" y1="7" x2="10" y2="10"/>
        <line x1="29" y1="7" x2="26" y2="10"/><line x1="2" y1="18" x2="6" y2="18"/>
        <line x1="7" y1="29" x2="10" y2="26"/>
      </g>
      <circle cx="18" cy="18" r="8" fill="#fff"/>
      <path d="M14 48 a9 9 0 0 1 2 -17 a13 13 0 0 1 25 -4 a10 10 0 0 1 17 8 a7 7 0 0 1 -2 13 z" fill="#fff" stroke="var(--hotel-band)" stroke-width="1.5"/>
    </svg>
    <div class="temp">18<span class="deg">°</span><span class="unit">C</span></div>
    <div class="clock">14:44<span class="meridiem">PM</span></div>
    <div class="weekday">SUNDAY</div>
    <div class="date">25 AUGUST</div>
    <svg class="wayfinder" viewBox="0 0 124 124" aria-label="Floor 12 up">
      <circle cx="60" cy="64" r="60" fill="var(--hotel-accent)"/>
      <circle cx="64" cy="60" r="56" fill="#fff"/>
      <polygon points="62,10 30,72 62,60" fill="var(--hotel-accent)"/>
      <polygon points="62,10 94,72 62,60" fill="var(--hotel-accent-dark)"/>
      <text x="62" y="110" text-anchor="middle" fill="var(--hotel-accent)">12</text>
    </svg>
  </section>

  <section class="display display--mall">
    <div class="photo" role="img" aria-label="Multi-level shopping mall atrium with escalators and hanging banners"></div>
    <div class="strip"></div>
    <div class="info-band"></div>
    <div class="brand">VELORA</div>
    <svg class="weather-icon" viewBox="0 0 62 52" aria-label="Sunny">
      <g stroke="#fff" stroke-width="2.2" stroke-linecap="round">
        <line x1="31" y1="0" x2="31" y2="7"/><line x1="31" y1="45" x2="31" y2="52"/>
        <line x1="3" y1="26" x2="11" y2="26"/><line x1="51" y1="26" x2="59" y2="26"/>
        <line x1="12" y1="8" x2="17" y2="13"/><line x1="50" y1="8" x2="45" y2="13"/>
        <line x1="12" y1="44" x2="17" y2="39"/><line x1="50" y1="44" x2="45" y2="39"/>
      </g>
      <circle cx="31" cy="26" r="14" fill="#fff"/>
    </svg>
    <div class="temp">30<span class="deg">°</span><span class="unit">C</span></div>
    <div class="clock">01:54<span class="meridiem">PM</span></div>
    <div class="weekday">THURSDAY</div>
    <div class="date">03 April</div>
    <svg class="wayfinder" viewBox="0 0 124 124" aria-label="Floor 5 up">
      <circle cx="60" cy="64" r="60" fill="var(--mall-accent)"/>
      <circle cx="64" cy="60" r="56" fill="#fff"/>
      <polygon points="62,10 30,72 62,60" fill="var(--mall-accent)"/>
      <polygon points="62,10 94,72 62,60" fill="var(--mall-accent-dark)"/>
      <text x="62" y="110" text-anchor="middle" fill="var(--mall-accent)">5</text>
    </svg>
  </section>

</main>
</body>
</html>
```